Eco friendly Swedish beauty products sold in aluminum bottles - label design needed

We need help in designing a series of stick on labels for 80 ml (2.7 fl. oz.) aluminum bottles containing beauty products such as soaps, shampoo etc. The diameter of the bottle is 36 mm and the body of the bottles measures approx. 106 mm.
It is important for us that the label has a simplistic and clean feel with few colors (and the right ones!) and that the label helps amplify this product being both better and a more sustainable alternative to many of our plastic bottle competitors. The design and label should communicate the feel of an Eco-friendly, sustainable and modern brand of high quality - and with a Swedish concept.
We are using Montserrat font in our materials. Find attached information of preferred colors, the bottles and one example of our logotype. I am also available on e-mail should further information be needed.

Looking forward and very excited to receive your suggestions.
Note that we are expecting to start selling a series of approximately 10 different products where I will need one "master design" and then only smaller changes for each of the different products.

Target Market(s)

People whom are aware and not only look at price tag. Private and commercial market.

Industry/Entity Type

Beauty

Font styles to use
Other font styles liked:
• Montserrat

Requirements
Must have
• It must give the feel of being both better and a more sustainable alternative to many of our plastic bottle competitors.
Nice to have
• Simplistic. Clean. Clear.
Should not have
• Wrong colors, too complex designs.

```html
<!DOCTYPE html>
<html lang="en">
<head>
<meta charset="utf-8">
<title>Vida Norr – Hair Shampoo Liquid label</title>
<link rel="stylesheet" href="https://fonts.googleapis.com/css2?family=Montserrat:wght@200;300;400;500;600;700;800&display=swap">
<style>
  :root {
    --label-bg: #333333;
    --ink-light: #e6e4e2;
    --rust: #a34a30;
    --sand: #e0b99b;
    --copper-rule: #c07a2a;
    --olive: #7a8040;
  }
  html, body {
    margin: 0;
    padding: 0;
    width: 1200px;
    height: 3535px;
    overflow: hidden;
    background: var(--label-bg);
  }
  .label {
    display: block;
    width: 1200px;
    height: 3535px;
    font-family: 'Montserrat', sans-serif;
  }
  .brand-name { fill: var(--ink-light); font-weight: 400; font-size: 74px; letter-spacing: 12px; }
  .brand-origin { fill: var(--ink-light); font-weight: 500; font-size: 24px; letter-spacing: 7px; }
  .volume-main { fill: var(--ink-light); font-weight: 300; font-size: 112px; letter-spacing: 2px; }
  .volume-sub { fill: var(--ink-light); font-weight: 400; font-size: 54px; }
  .volume-rule { stroke: var(--copper-rule); stroke-width: 4; }
  .title-light { fill: var(--rust); font-weight: 200; font-size: 278px; }
  .title-bold { fill: var(--rust); font-weight: 800; font-size: 278px; }
  .variant { fill: var(--sand); font-weight: 300; font-size: 228px; }
  .natural-percent { fill: var(--olive); font-weight: 800; font-size: 72px; }
  .natural-word { fill: var(--olive); font-weight: 600; font-size: 62px; letter-spacing: 22px; }
  .natural-caption { fill: var(--olive); font-weight: 400; font-size: 35px; }
  .natural-sprig { fill: var(--olive); opacity: 0.45; }
</style>
</head>
<body>
<svg class="label" viewBox="0 0 1200 3535" xmlns="http://www.w3.org/2000/svg">
  <rect width="1200" height="3535" fill="var(--label-bg)"/>

  <g class="brand">
    <text class="brand-name" x="1030" y="593" text-anchor="end">VIDA NORR</text>
    <text class="brand-origin" x="1030" y="655" text-anchor="end">SWEDEN</text>
  </g>

  <g class="volume">
    <text class="volume-main" x="1030" y="940" text-anchor="end">80 ML</text>
    <text class="volume-sub" x="1030" y="1003" text-anchor="end">(2.7 FL. OZ.)</text>
    <line class="volume-rule" x1="556" y1="1031" x2="1030" y2="1031"/>
  </g>

  <g class="product-title">
    <text transform="translate(362 3130) rotate(-90)">
      <tspan class="title-light">HAIR</tspan><tspan class="title-bold" dx="30">SHAMPOO</tspan>
    </text>
    <text class="variant" transform="translate(566 3112) rotate(-90)">LIQUID</text>
  </g>

  <g class="natural-badge">
    <text class="natural-percent" transform="translate(757 3080) rotate(-90)">100%</text>
    <text class="natural-word" x="768" y="2909">NAT</text>
    <text class="natural-word" x="768" y="3008">URAL</text>
    <text class="natural-caption" x="768" y="3087">INGREDIENTS</text>
    <ellipse class="natural-sprig" role="img" aria-label="Small botanical sprig illustration" cx="990" cy="2885" rx="40" ry="60"/>
  </g>
</svg>
</body>
</html>
```